Rock climbing centre flyer

We need a general flyer for our rock climbing gym that we can use for general advertising inside and outside the gym.

Target Market(s)

Fitness enthusiasts, dare devils, people willing to try something different

Industry/Entity Type

Fitness

Font styles to use
Other font styles liked:
• Any kind of distressed font

Colors
cadf82
eaf2ce
e9e9e9
474747

Requirements
Must have
• Double sided flyer
• Main tag line should be "No strings attached"
• Ridgeway Ascent logo
• Large imagery
• Address: 4/61 Willowby Lane East Harrowgate
• Phone: 9417 5830
• Email: info@ridgewayascent.example.com.au
• Opening hours (find from the website ridgewayascent.example.com.au)
• List our services:
• Unlimited bouldering
• Strength & Conditioning
• Yoga
• Birthday parties & group activities
• Kids coaching and specialist technique training
• View our timetable online at ridgewayascent.example.com.au
• Find us on Facebook Ridgeway Ascent Centre

```html
<!DOCTYPE html>
<html lang="en">
<head>
<meta charset="utf-8">
<title>Our Services – Ridgeway Ascent</title>
<link href="https://fonts.googleapis.com/css2?family=Bebas+Neue&family=Catamaran:wght@500;600&display=swap" rel="stylesheet">
<style>
  :root {
    --lime: #cadf82;
    --lime-pale: #eaf2ce;
    --paper: #e9e9e9;
    --graphite: #474747;
    --ink: #000;
    --white: #fff;
    --wall-grey: #8e8c8d;
    --wall-dark: #4e4c4d;
    --volume-yellow: #c9c15a;
    --volume-orange: #c8692e;
  }
  html, body { margin: 0; padding: 0; overflow: hidden; }
  .flyer {
    position: relative;
    width: 846px;
    height: 1200px;
    overflow: hidden;
    background: var(--paper);
    font-family: "Catamaran", sans-serif;
  }
  .backdrop { position: absolute; inset: 0; }
  .backdrop--front { z-index: 3; pointer-events: none; }
  .title {
    position: absolute;
    left: 52px;
    top: 74px;
    margin: 0;
    font-family: "Bebas Neue", sans-serif;
    font-weight: 400;
    font-size: 100px;
    line-height: 1;
    letter-spacing: 0;
    color: var(--ink);
    text-shadow: 2px 3px 3px rgba(0,0,0,.35);
  }
  .title .accent { color: var(--lime); }
  .rule {
    position: absolute;
    left: 0; top: 171px;
    width: 846px; height: 5px;
    background: var(--lime);
  }
  .panel {
    position: absolute;
    background: var(--ink);
    color: var(--white);
    z-index: 2;
  }
  .panel--services { left: 0; top: 176px; width: 426px; height: 316px; }
  .panel--coaching { left: 432px; top: 816px; width: 414px; height: 164px; }
  .divider {
    position: absolute;
    left: 426px; top: 176px;
    width: 6px; height: 804px;
    background: var(--lime);
    z-index: 2;
  }
  .service-list {
    list-style: none;
    margin: 0;
    padding: 0;
    position: absolute;
  }
  .panel--services .service-list { left: 42px; top: 24px; }
  .panel--coaching .service-list { left: 40px; top: 28px; }
  .service-list li {
    position: relative;
    padding-left: 44px;
    font-size: 28px;
    font-weight: 600;
    line-height: 36px;
    margin-bottom: 29px;
    white-space: nowrap;
  }
  .service-list li svg {
    position: absolute;
    left: 0; top: 2px;
    width: 26px; height: 26px;
  }
  .photo { position: absolute; z-index: 1; }
  .photo--climber-overhang {
    left: 0; top: 492px; width: 426px; height: 480px;
    background:
      radial-gradient(ellipse 120px 160px at 40px 120px, rgba(200,105,46,.75), transparent 70%),
      radial-gradient(ellipse 150px 70px at 70px 330px, rgba(201,193,90,.8), transparent 70%),
      radial-gradient(ellipse 140px 200px at 260px 280px, rgba(245,245,245,.55), transparent 70%),
      linear-gradient(180deg, #b9b7b9 0%, #a7a5a8 45%, #6d6a6d 78%, #4a4748 100%);
  }
  .photo--climber-wall {
    left: 432px; top: 176px; width: 414px; height: 640px;
    background:
      radial-gradient(ellipse 170px 190px at 70px 90px, rgba(201,193,90,.85), transparent 72%),
      radial-gradient(ellipse 130px 200px at 250px 220px, rgba(170,205,80,.55), transparent 70%),
      radial-gradient(ellipse 90px 220px at 110px 560px, rgba(200,105,46,.75), transparent 70%),
      radial-gradient(ellipse 70px 140px at 400px 560px, rgba(201,193,90,.7), transparent 70%),
      linear-gradient(200deg, #b2b1b3 0%, #9a989a 40%, #7b797a 75%, #5b595a 100%);
  }
  .contact {
    position: absolute;
    right: 46px;
    top: 1084px;
    text-align: right;
    font-size: 19px;
    font-weight: 500;
    line-height: 40px;
    color: var(--ink);
    z-index: 4;
  }
  .contact p { margin: 0; }
  .contact .link { text-decoration: underline; }
</style>
</head>
<body>
<div class="flyer">
  <svg class="backdrop" width="846" height="1200" viewBox="0 0 846 1200" aria-hidden="true">
    <polygon points="0,0 512,0 0,64" fill="var(--lime)"/>
    <polygon points="380,0 846,0 846,24 470,14" fill="var(--ink)"/>
    <polygon points="250,34 846,20 846,150" fill="var(--graphite)"/>
  </svg>

  <h1 class="title">Our <span class="accent">Services</span></h1>
  <div class="rule"></div>

  <section class="panel panel--services">
    <ul class="service-list">
      <li><svg viewBox="0 0 26 26"><path d="M2 14 L9 22 L24 3" fill="none" stroke="var(--lime)" stroke-width="3"/></svg>Unlimited bouldering</li>
      <li><svg viewBox="0 0 26 26"><path d="M2 14 L9 22 L24 3" fill="none" stroke="var(--lime)" stroke-width="3"/></svg>Strength &amp; Conditioning</li>
      <li><svg viewBox="0 0 26 26"><path d="M2 14 L9 22 L24 3" fill="none" stroke="var(--lime)" stroke-width="3"/></svg>Yoga</li>
      <li><svg viewBox="0 0 26 26"><path d="M2 14 L9 22 L24 3" fill="none" stroke="var(--lime)" stroke-width="3"/></svg>Birthday parties &amp;<br>group activities</li>
    </ul>
  </section>

  <div class="divider"></div>

  <div class="photo photo--climber-wall" role="img" aria-label="Photo of a climber in a green shirt on a steep indoor bouldering wall with yellow and orange volumes"></div>
  <div class="photo photo--climber-overhang" role="img" aria-label="Photo of a climber in a white singlet hanging from holds on an overhanging grey wall"></div>

  <section class="panel panel--coaching">
    <ul class="service-list">
      <li><svg viewBox="0 0 26 26"><path d="M2 14 L9 22 L24 3" fill="none" stroke="var(--lime)" stroke-width="3"/></svg>Kids coaching and<br>specialist technique<br>training</li>
    </ul>
  </section>

  <svg class="backdrop backdrop--front" width="846" height="1200" viewBox="0 0 846 1200" aria-hidden="true">
    <polygon points="0,944 846,1000 846,1012 0,1020" fill="var(--graphite)"/>
    <polygon points="584,980 846,912 846,1000" fill="var(--lime)"/>
    <polygon points="0,1020 846,1008 846,1030 0,1118" fill="var(--ink)"/>
  </svg>

  <footer class="contact">
    <p>View our timetable online at <span class="link">ridgewayascent.example.com.au</span></p>
    <p>Find us on Facebook Ridgeway Ascent Centre</p>
  </footer>
</div>
</body>
</html>
```